New corporate e-mail signature

We need a new e-mail signature for our company that is clean and professional. The requests are attached in a document.

Target Market(s)

CFO, CTO, Controllers, leaders, decision-makers.

Industry/Entity Type

Information Technology

Colors

Designer to choose colors to be used in the design.

Requirements
Must have
• See the PowerPoint document.
• - keep it as simple as possible.
• - same style as our new website design
• - It has to look good in all e-mail readers, and on all surfaces.
Nice to have
• - Please also attach 'best practise' for how to use the signature.
Should not have
• See the PowerPoint document. Use our color palette.
• - Do not include photo!

```html
<!DOCTYPE html>
<html lang="en">
<head>
<meta charset="utf-8">
<title>Ledgerpoint e-mail signature</title>
<link rel="stylesheet" href="https://fonts.googleapis.com/css2?family=Open+Sans:wght@400&display=swap">
<style>
  :root {
    --navy: #0a2d5e;
    --blue: #2e90cf;
    --teal: #1f7aa0;
    --icon: #1f6f93;
    --orange: #f39c4f;
    --text: #1a1a1a;
    --paper: #ffffff;
  }
  * { box-sizing: border-box; margin: 0; padding: 0; }
  html, body { width: 1200px; height: 330px; overflow: hidden; background: var(--paper); }
  body { font-family: "Open Sans", "Segoe UI", sans-serif; color: var(--text); }
  .signature { position: relative; width: 1200px; height: 330px; overflow: hidden; background: var(--paper); }
  .top-band {
    position: absolute; left: 0; top: 0; width: 495px; height: 19px;
    background: linear-gradient(90deg, var(--navy) 0%, var(--navy) 30%, var(--blue) 100%);
  }
  .bottom-rule { position: absolute; left: 0; top: 318px; width: 1200px; height: 4px; background: var(--orange); }
  .bottom-band {
    position: absolute; left: 0; top: 322px; width: 1200px; height: 8px;
    background: linear-gradient(90deg, var(--navy) 0%, var(--navy) 55%, var(--blue) 100%);
  }
  .details { position: absolute; font-size: 20px; line-height: 1; }
  .details li { list-style: none; height: 39.5px; display: flex; align-items: center; }
  .person { left: 25px; top: 81px; }
  .contact { left: 569px; top: 81px; }
  .contact .icon { width: 25px; height: 25px; margin-right: 8px; flex: none; }
  .follow {
    position: absolute; left: 19px; top: 257px; height: 43px;
    display: flex; align-items: center; font-size: 20px;
  }
  .follow-label { margin-right: 22px; }
  .network { display: flex; align-items: center; margin-right: 18px; color: var(--orange); font-size: 20px; }
  .network-square { width: 30px; height: 30px; background: var(--orange); border-radius: 2px; margin-right: 8px; }
  .corner-accent {
    position: absolute; right: 0; top: 125px; width: 170px; height: 193px;
    background: linear-gradient(160deg, rgba(31,122,160,0) 10%, rgba(31,122,160,0.55) 60%, var(--teal) 100%);
    clip-path: polygon(100% 0, 100% 100%, 0 100%);
  }
</style>
</head>
<body>
<main class="signature">
  <div class="top-band"></div>

  <ul class="details person">
    <li>Name:</li>
    <li>Role:</li>
    <li>Company:&nbsp;Ledgerpoint</li>
  </ul>

  <ul class="details contact">
    <li>
      <svg class="icon" viewBox="0 0 24 24" aria-hidden="true">
        <circle cx="12" cy="12" r="10.5" fill="none" stroke="var(--icon)" stroke-width="1.6"/>
        <path d="M8.2 6.5c.6-.4 1.2-.3 1.5.2l1.1 1.9c.3.5.1 1-.3 1.3l-.7.5c.5 1.4 1.4 2.6 2.7 3.4l.6-.6c.4-.4 1-.4 1.4 0l1.6 1.4c.4.4.4 1 0 1.4l-.8.8c-.6.6-1.6.7-2.4.3-2.8-1.5-4.7-3.9-5.5-6.9-.2-.8.1-1.6.8-2.1z" fill="var(--icon)"/>
      </svg>
      Mob:
    </li>
    <li>
      <svg class="icon" viewBox="0 0 24 24" aria-hidden="true">
        <rect x="1" y="5" width="22" height="14" fill="var(--icon)"/>
        <path d="M1 5l11 8 11-8" fill="none" stroke="var(--paper)" stroke-width="1.4"/>
      </svg>
      Email:
    </li>
    <li>
      <svg class="icon" viewBox="0 0 24 24" aria-hidden="true">
        <g fill="none" stroke="var(--icon)" stroke-width="1.2">
          <circle cx="12" cy="12" r="10"/>
          <ellipse cx="12" cy="12" rx="4.5" ry="10"/>
          <path d="M2 12h20M3.5 7h17M3.5 17h17"/>
        </g>
      </svg>
      www.ledgerpoint.com
    </li>
  </ul>

  <div class="follow">
    <span class="follow-label">Follow ledgerpoint on:</span>
    <span class="network"><span class="network-square"></span>Linkora</span>
    <span class="network"><span class="network-square"></span>Facemeet</span>
  </div>

  <div class="corner-accent" role="img" aria-label="Angular blue brand accent shapes rising from the lower right corner"></div>

  <div class="bottom-rule"></div>
  <div class="bottom-band"></div>
</main>
</body>
</html>
```